Web page design for a startup, no coding

Quillbrook is a Data mining startup helping companies get data from websites. We’re looking to revamp our website to make it more professional and conversation friendly.
I need a designer to design the website in PSD and Once the PSD is done, the HTML design will be awarded as a separate job. We’ll need continues improvements to the design based on the user behaviour in the site and this can be a long term work for the right designer.
Read the details on the attached document
Target Market(s)
Big data, Data Mining
Industry/Entity Type
Business Software
Number of Pages Required
5+ page
Requirements
Must have
- Refer to the doc
Nice to have
- Refer to the doc
Should not have
- Refer to the doc

```html
<!DOCTYPE html>
<html lang="en">
<head>
<meta charset="utf-8">
<title>Quillbrook — Structured Data Feeds</title>
<link href="https://fonts.googleapis.com/css2?family=Roboto+Condensed:wght@400;700&family=Open+Sans:ital,wght@0,400;0,600;1,400&display=swap" rel="stylesheet">
<style>
:root{
  --sky:#4fb4ee;
  --sky-light:#7cc8f3;
  --navy:#1d4f8c;
  --navy-dark:#17457d;
  --ink:#333;
  --muted:#666;
  --soft:#f3f4f5;
  --line:#d6d9dc;
  --foot:#343434;
  --foot-dark:#232323;
  --white:#fff;
}
*{box-sizing:border-box;margin:0;padding:0}
html,body{width:1200px;height:3237px;overflow:hidden}
body{position:relative;font-family:"Open Sans",sans-serif;color:var(--ink);background:var(--white)}
.abs{position:absolute}
.head{font-family:"Roboto Condensed",sans-serif}

/* hero */
.hero{left:0;top:0;width:1200px;height:561px;background:radial-gradient(circle at 70% 40%,var(--sky-light),var(--sky) 70%)}
.brand{left:155px;top:22px;display:flex;align-items:center;gap:12px;color:var(--white);font-family:"Roboto Condensed",sans-serif;font-size:40px}
.brand i{width:34px;height:34px;border:3px solid var(--white);border-radius:50%}
.auth{top:17px;height:31px;width:82px;font-size:13px;display:flex;align-items:center;justify-content:center;border:1px solid var(--white)}
.auth.login{left:874px;background:var(--white);color:var(--sky)}
.auth.signup{left:962px;color:var(--white)}
.nav{left:725px;top:60px;display:flex;gap:30px;font-size:13px;font-weight:600;color:var(--white)}
.nav span.on{border-bottom:2px solid var(--white);padding-bottom:4px}
.hero h1{left:155px;top:205px;font-size:39px;line-height:48px;font-weight:400;color:var(--white);letter-spacing:1px}
.hero h1 b{color:var(--navy);font-weight:400}
.hero p{left:155px;top:310px;width:520px;font-size:14px;line-height:20px;color:var(--white)}
.btn{background:var(--navy);color:var(--white);font-size:13px;display:flex;align-items:center;justify-content:center;gap:6px}
.hero .btn{left:155px;top:390px;width:127px;height:35px}
.hero-photo{left:701px;top:173px;width:270px;height:388px;background:linear-gradient(180deg,#c9d7e3,#3f7fc0);border-radius:120px 120px 0 0}
.arrow{stroke:var(--white);stroke-width:3;fill:none}

/* partners */
.partners{left:0;top:561px;width:1200px;height:142px;background:var(--soft);display:flex;justify-content:center;align-items:center;gap:64px;font-family:"Roboto Condensed",sans-serif;font-size:30px;color:#9a9a9a}
.partners .hl{color:var(--navy)}

/* sections */
.title{width:1200px;left:0;text-align:center;font-family:"Roboto Condensed",sans-serif;font-size:25px;color:var(--navy)}
.sub{left:300px;width:600px;text-align:center;font-size:13px;line-height:20px;color:var(--muted)}
.sol{width:200px}
.sol h3{display:flex;align-items:center;gap:10px;font-family:"Roboto Condensed",sans-serif;font-size:16px;font-weight:400;color:var(--ink);height:42px}
.sol p{margin-top:12px;font-size:11.5px;line-height:18px;color:var(--muted)}
.sol .more{margin-top:14px;display:block}
.sol-art{left:831px;top:874px;width:226px;height:270px;background:radial-gradient(circle at 50% 35%,#cfe6f7,#f6f9fb 70%)}

.why{left:0;top:1226px;width:1200px;height:518px;background:linear-gradient(180deg,#f4f5f6,#eceef0)}
.why-art{left:155px;top:1349px;width:417px;height:281px;background:linear-gradient(160deg,#e4e8ec,#b7c4d1);border-radius:14px}
.why-item{left:613px;width:430px;display:flex;gap:14px}
.why-item h4{font-family:"Roboto Condensed",sans-serif;font-size:15px;font-weight:700;color:var(--ink)}
.why-item p{margin-top:4px;font-size:11.5px;line-height:18px;color:var(--muted);height:36px;overflow:hidden}

.field{height:39px;border:1px solid var(--line);font-size:11.5px;color:#888;display:flex;align-items:center;justify-content:space-between;padding:0 22px}
.field.area{align-items:flex-start;padding-top:14px}

.subscribe{left:0;top:2305px;width:1200px;height:203px;background:radial-gradient(circle at 50% 50%,var(--sky-light),var(--sky) 70%)}

.footer{left:0;top:2918px;width:1200px;height:248px;background:var(--foot);color:#bbb;font-size:12px}
.footer h5{font-size:13px;font-weight:600;color:var(--white);margin-bottom:16px}
.footer .col{position:absolute;top:50px;line-height:17px}
.bottom{left:0;top:3166px;width:1200px;height:71px;background:var(--foot-dark);color:#ccc;font-size:12px}
</style>
</head>
<body>

<section class="abs hero">
  <div class="abs brand"><i></i>quillbrook</div>
  <div class="abs auth login">Login</div>
  <div class="abs auth signup">Signup</div>
  <nav class="abs nav"><span class="on">Solutions</span><span>Pricing</span><span>Company</span><span>Get free Quote</span></nav>
  <h1 class="abs head">GET STRUCTURED DATA <b>FEEDS</b><br>FROM <b>ANY</b> WEBSITE</h1>
  <p class="abs">Quillbrook provides a cloud based data as a service platform to help companies get data feeds from any website easily. No coding ,Servers or Softwares required.</p>
  <div class="abs btn">Get Started &#9758;</div>
  <div class="abs hero-photo" role="img" aria-label="Smiling man holding a laptop showing a data dashboard"></div>
  <svg class="abs" style="left:100px;top:250px" width="30" height="60"><path class="arrow" d="M26 4 L4 30 L26 56"/></svg>
  <svg class="abs" style="left:1070px;top:250px" width="30" height="60"><path class="arrow" d="M4 4 L26 30 L4 56"/></svg>
</section>

<section class="abs partners">
  <span>Vantoria</span><span>Meridex</span><span>Kelvane</span><span class="hl">Orbisly</span><span>Launchfield</span><span>Halvorsen</span>
</section>

<h2 class="abs title" style="top:753px">Our Solutions</h2>
<p class="abs sub" style="top:790px">Businesses of all sizes use our clean data feeds to Quickly build apps, Experiment with fresh ideas and Solve business problems.</p>

<div class="abs sol" style="left:155px;top:855px">
  <h3><svg width="40" height="40" fill="none" stroke="#1d88d8" stroke-width="2.5"><rect x="4" y="6" width="30" height="20"/><path d="M14 34h10M19 26v8"/></svg>ECommerce</h3>
  <p>Our Ecommerce product data feeds gives you access to structured product information like pricing, Category, reviews etc about your competitors.</p>
  <svg class="more" width="26" height="8"><path d="M0 4h22M18 1l4 3-4 3" stroke="#555" fill="none"/></svg>
</div>
<div class="abs sol" style="left:384px;top:855px">
  <h3><svg width="40" height="40" fill="none" stroke="#1d88d8" stroke-width="2.5"><path d="M4 30l10-10 8 6 14-14M28 12h8v8"/></svg>Lead generation</h3>
  <p>We help find quality leads for your business by extracting public data from all kind of sources like Profilenet, Fundbase, Seedlist etc.</p>
  <svg class="more" width="26" height="8"><path d="M0 4h22M18 1l4 3-4 3" stroke="#555" fill="none"/></svg>
</div>
<div class="abs sol" style="left:611px;top:855px">
  <h3><svg width="40" height="40" fill="none" stroke="#1d88d8" stroke-width="2.5"><circle cx="16" cy="16" r="10"/><path d="M24 24l12 12"/></svg>SERP Tracking</h3>
  <p>Our SERP data feeds gives companies access to Search Engine rankings of any keywords from search engines like Searchly, Findora and Lookwise.</p>
  <svg class="more" width="26" height="8"><path d="M0 4h22M18 1l4 3-4 3" stroke="#555" fill="none"/></svg>
</div>
<div class="abs sol" style="left:155px;top:1031px">
  <h3><svg width="40" height="40" fill="none" stroke="#1d88d8" stroke-width="2.5"><circle cx="20" cy="20" r="8"/><path d="M20 4v6M20 30v6M4 20h6M30 20h6"/></svg>News Aggregation</h3>
  <p>We help businesses build their own unique news data feeds by aggregating data from news sites, industry blogs etc.</p>
  <svg class="more" width="26" height="8"><path d="M0 4h22M18 1l4 3-4 3" stroke="#555" fill="none"/></svg>
</div>
<div class="abs sol" style="left:384px;top:1031px">
  <h3><svg width="40" height="40" fill="none" stroke="#1d88d8" stroke-width="2.5"><circle cx="12" cy="12" r="5"/><circle cx="28" cy="12" r="5"/><path d="M3 34c0-8 18-8 18 0M19 34c0-8 18-8 18 0"/></svg>Recruiting</h3>
  <p>We help recruiters automate scouting candidate profiles from different online sources and speed up hiring process.</p>
  <svg class="more" width="26" height="8"><path d="M0 4h22M18 1l4 3-4 3" stroke="#555" fill="none"/></svg>
</div>
<div class="abs sol" style="left:611px;top:1031px">
  <h3><svg width="40" height="40" fill="none" stroke="#1d88d8" stroke-width="2.5"><rect x="10" y="4" width="20" height="32" rx="3"/><path d="M17 30h6"/></svg>Build your App</h3>
  <p>We help businesses quickly build their apps on top of our scalable data extraction infrastructure.</p>
  <svg class="more" width="26" height="8"><path d="M0 4h22M18 1l4 3-4 3" stroke="#555" fill="none"/></svg>
</div>
<div class="abs sol-art" role="img" aria-label="Illustration of a person relaxing at a desk beneath a cloud of app icons"></div>

<section class="abs why"></section>
<h2 class="abs title" style="top:1275px">Why Quillbrook ?</h2>
<div class="abs why-art" role="img" aria-label="Tablet showing a data table with product image cards floating above"></div>
<div class="abs why-item" style="top:1328px">
  <svg width="22" height="22"><rect x="1" y="1" width="20" height="20" fill="#2a94db"/><path d="M5 11l4 4 8-9" stroke="#fff" stroke-width="2.5" fill="none"/></svg>
  <div><h4>Solve real problems</h4><p>Quillbrook provides a fully managed Big Data As A Service. You can easily plug our data feeds into your favourite tool and start solving the real problems.</p><svg width="26" height="8"><path d="M0 4h22M18 1l4 3-4 3" stroke="#555" fill="none"/></svg></div>
</div>
<div class="abs why-item" style="top:1423px">
  <svg width="22" height="22"><rect x="1" y="1" width="20" height="20" fill="#2a94db"/><path d="M5 11l4 4 8-9" stroke="#fff" stroke-width="2.5" fill="none"/></svg>
  <div><h4>Clean Data</h4><p>We follow a strict quality assurance process and a Machine learning based Q&amp;A system to ensure the data integrity. You can export data as needed.</p><svg width="26" height="8"><path d="M0 4h22M18 1l4 3-4 3" stroke="#555" fill="none"/></svg></div>
</div>
<div class="abs why-item" style="top:1518px">
  <svg width="22" height="22"><rect x="1" y="1" width="20" height="20" fill="#2a94db"/><path d="M5 11l4 4 8-9" stroke="#fff" stroke-width="2.5" fill="none"/></svg>
  <div><h4>Customer Success:</h4><p>Ensuring Customer success is our first priority. Our customer success team consists of experienced data mining engineers and they are ready to help.</p><svg width="26" height="8"><path d="M0 4h22M18 1l4 3-4 3" stroke="#555" fill="none"/></svg></div>
</div>
<div class="abs why-item" style="top:1613px">
  <svg width="22" height="22"><rect x="1" y="1" width="20" height="20" fill="#2a94db"/><path d="M5 11l4 4 8-9" stroke="#fff" stroke-width="2.5" fill="none"/></svg>
  <div><h4>Data Wrangling support</h4><p>Quillbrook helps those who need data wrangling support by providing profiling, filtering and enrichment support. We know just getting structured data is not enough.</p><svg width="26" height="8"><path d="M0 4h22M18 1l4 3-4 3" stroke="#555" fill="none"/></svg></div>
</div>

<h2 class="abs title" style="top:1796px">We’re here to help!</h2>
<p class="abs sub" style="top:1833px">“ We're friendly and available to help solve your data extraction problems. Fill the form below to contact us. Let us do the heavy lifting for you.”</p>
<div class="abs field" style="left:155px;top:1899px;width:432px">Enter Your Name<svg width="14" height="14" fill="#999"><circle cx="7" cy="4" r="3.5"/><path d="M0 14c0-6 14-6 14 0z"/></svg></div>
<div class="abs field" style="left:613px;top:1899px;width:431px;border-color:#bbb">Enter Your Email Address<svg width="18" height="13" fill="none" stroke="#444" stroke-width="1.5"><rect x="1" y="1" width="16" height="11"/><path d="M1 1l8 6 8-6"/></svg></div>
<div class="abs field" style="left:155px;top:1962px;width:432px">Enter Your Phone Number<svg width="14" height="14" fill="#999"><circle cx="7" cy="4" r="3.5"/><path d="M0 14c0-6 14-6 14 0z"/></svg></div>
<div class="abs field" style="left:613px;top:1962px;width:431px">Enter Your Monthly Budget<svg width="12" height="8" fill="none" stroke="#888" stroke-width="1.5"><path d="M1 1l5 5 5-5"/></svg></div>
<div class="abs field area" style="left:155px;top:2024px;width:889px;height:162px">Drop us a line or two, We will get back to you Soon...</div>
<div class="abs btn" style="left:155px;top:2210px;width:127px;height:35px">Send Message &#10148;</div>

<section class="abs subscribe">
  <h2 class="abs title" style="top:48px;color:var(--navy-dark);font-size:24px">Subscribe to our blog</h2>
  <div class="abs" style="left:319px;top:106px;width:432px;height:39px;background:#fff;font-size:11.5px;color:#888;padding:12px 16px">Enter Your Email Address</div>
  <div class="abs btn" style="left:751px;top:106px;width:127px;height:39px">Subscribe Now</div>
</section>

<h2 class="abs title" style="top:2557px">“ What Our Clients Says ? ”</h2>
<div class="abs" style="left:555px;top:2614px;width:94px;height:94px;border-radius:50%;background:linear-gradient(#8a8a8a,#3a3a3a);border:3px solid #ddd" role="img" aria-label="Client portrait"></div>
<p class="abs sub" style="left:320px;width:560px;top:2738px;font-style:italic;font-size:12.5px">Data extraction can vary greatly in price. I have personally reviewed over 30 companies that provide data extraction services and Quillbrook is the most competitive in price and offer the best service. They know what they are doing...</p>
<p class="abs title" style="top:2817px;font-size:20px;color:var(--navy)">Marcus Hale</p>
<p class="abs title" style="top:2850px;font-family:'Open Sans',sans-serif;font-size:12px;color:var(--muted)">- Co-founder of Rankwise Labs -</p>
<svg class="abs" style="left:128px;top:2770px" width="20" height="40"><path d="M18 2L2 20l16 18" stroke="#333" stroke-width="2" fill="none"/></svg>
<svg class="abs" style="left:1044px;top:2770px" width="20" height="40"><path d="M2 2l16 18L2 38" stroke="#4fb4ee" stroke-width="2" fill="none"/></svg>

<footer class="abs footer">
  <div class="col" style="left:155px;width:290px">
    <h5>LEADPAIL</h5>
    <p>Stop wasting time researching leads.<br>Leadpail is here to help.</p>
    <div style="margin-top:12px;width:280px;height:30px;border:1px solid #777;padding:6px 10px;color:#aaa;font-size:11px">Enter Your Email</div>
    <h5 style="margin-top:20px;margin-bottom:8px">GET SOCIAL</h5>
    <svg width="110" height="12" fill="#4fb4ee"><circle cx="6" cy="6" r="5"/><circle cx="24" cy="6" r="5"/><circle cx="42" cy="6" r="5"/><circle cx="60" cy="6" r="5"/><circle cx="78" cy="6" r="5"/><circle cx="96" cy="6" r="5"/></svg>
  </div>
  <div class="col" style="left:511px">
    <h5>QUICK LINKS</h5>
    <p style="color:var(--sky)">Blog</p><p>Startup Partner program</p><p>Answers</p><p>FAQ</p><p>Case Studies</p><p>Careers</p><p>Slide</p><p>Social media link</p>
  </div>
  <div class="col" style="left:686px;width:300px">
    <h5>KEEP IN TOUCH</h5>
    <p style="color:var(--sky)">Address :</p>
    <p>418 Harbor View Road Suite C-4 Millbrook, Delaware 19811 United States</p>
    <h5 style="margin-top:14px;margin-bottom:4px">CONTACT US</h5>
    <p style="color:var(--sky);font-size:24px;line-height:30px">+01 555 - 01234</p>
    <p>info@quillbrook.co</p>
  </div>
</footer>
<div class="abs bottom">
  <p class="abs" style="left:155px;top:28px">© 2016 <span style="color:var(--sky)">Quillbrook</span>. All rights reserved.</p>
  <svg class="abs" style="left:1008px;top:18px" width="36" height="36" fill="none" stroke="#4fb4ee" stroke-width="1.5"><circle cx="18" cy="18" r="16"/><path d="M12 21l6-6 6 6"/></svg>
</div>

</body>
</html>
```